family chiropractic health care team needs a modern business card design

Healthcare office with Chiropractors, Physiotherapists, Massage therapists and possibly other practitioners in the future. This is a friendly family office with patients of all ages (and lots of kids) that just moved into a new larger modern office.
Look at the website for photos of the office.
Design for the front and back of a business card required.
Text for the front:
Office logo and name of the office:
Bright Path Wellness Centre
Name of current Practitioner:
Dr. Marten Quovel B.Sc., D.C. Chiropractor
(But please include options to swap out name and title for other practitioners )

address:
218 Farrow Gate
Westmere ON.
K2J 6P4
Phone: 416-872-0196 (PATH)
Web site and email:
www.brightpathwellnesscentre.example
brightpathchiro@mailbox.example

2 versions of the back of the card:
1. text below
2. appointment schedule card

Text on back of card:
Chiropractic Card text on back of the card:
There is more to chiropractic than the relief of headaches and back pain! Our primary focus is the integrity of your nerve system, which controls and regulates every cell and tissue of your body. The moving bones of the spinal column can impair this vital communication link between your brain and body. We help improve the function and structure of your spine, reducing nerve system compromise. The result?
Even non-spinal related health problems can show improvement
without drugs
without surgery
regardless of age
for over a century
naturally

Appointment Card info For Back:
Please integrate design elements from the front of the card into an appointment card format.
M Tu W Th F Sat (and a line for writing on beside each one)

```html
<!DOCTYPE html>
<html lang="en">
<head>
<meta charset="utf-8">
<title>Bright Path Wellness Centre – Business Cards</title>
<link rel="stylesheet" href="https://fonts.googleapis.com/css2?family=Cinzel:wght@600&family=EB+Garamond:wght@400;500&display=swap">
<style>
  :root{
    --bg:#3a3a3a;
    --card-dark:#2b2b2b;
    --card-darker:#1d1d1d;
    --green:#8cc540;
    --white:#ffffff;
    --ink:#222222;
  }
  *{box-sizing:border-box;margin:0;padding:0}
  html,body{width:800px;height:1200px;overflow:hidden;background:var(--bg)}
  .sheet{position:relative;width:800px;height:1200px}
  .card{position:absolute;left:90px;width:620px;height:354px;border-radius:18px;overflow:hidden;box-shadow:0 6px 18px rgba(0,0,0,.45)}
  .card--front{top:30px}
  .card--info{top:418px}
  .card--appointment{top:806px;background:var(--white)}
  .card-bg{position:absolute;inset:0;width:100%;height:100%}
  .brand{position:absolute;display:flex;align-items:center;gap:10px;font-family:"Cinzel",serif;font-weight:600;color:var(--green);line-height:1.1}
  .brand-dot{flex:none;width:14px;height:14px;border-radius:50%;background:var(--green)}

  /* front */
  .card--front .brand{left:40px;top:70px;font-size:27px;width:330px}
  .practitioner{position:absolute;left:40px;top:218px;width:250px;font-family:"EB Garamond",serif;color:var(--white)}
  .practitioner-name{font-family:"Cinzel",serif;font-weight:600;font-size:15px;letter-spacing:.3px;white-space:nowrap}
  .practitioner-title{font-family:"Cinzel",serif;font-weight:600;font-size:16px;color:var(--green);margin-top:2px}
  .address{font-size:16px;line-height:1.25;margin-top:8px}
  .divider{position:absolute;background:var(--green);width:1.5px}
  .card--front .divider{left:300px;top:258px;height:80px}
  .contact{position:absolute;left:318px;top:262px;list-style:none;font-family:"EB Garamond",serif;font-size:15.5px;color:var(--white);line-height:1.55}
  .contact li{display:flex;align-items:center;gap:9px;white-space:nowrap}
  .contact svg{flex:none;width:13px;height:13px}

  /* info back */
  .card--info .brand{left:30px;top:135px;width:160px;font-size:20px;flex-direction:column;align-items:flex-start}
  .brand-dot--lg{width:40px;height:40px}
  .card--info .divider{left:210px;top:40px;height:250px}
  .info-text{position:absolute;left:228px;top:38px;width:350px;font-family:"EB Garamond",serif}
  .info-text p{font-size:12.4px;line-height:1.3;color:var(--green)}
  .benefits{list-style:none;margin-top:10px;font-size:14px;line-height:1.35;color:var(--white)}

  /* appointment back */
  .card--appointment .brand{left:40px;top:44px;font-size:24px;width:300px}
  .field{position:absolute;display:flex;align-items:flex-end;gap:8px;font-family:"EB Garamond",serif;font-size:15px;color:var(--ink)}
  .field-line{flex:1;border-bottom:1px solid var(--ink);height:1px}
  .field--name{left:40px;top:160px;width:520px}
  .field--note{left:40px;top:296px;width:520px}
  .days{position:absolute;left:40px;top:226px;width:520px;display:flex;justify-content:space-between;list-style:none;font-family:"EB Garamond",serif;font-size:14px;color:var(--ink)}
  .days li{display:flex;align-items:flex-start;gap:6px}
  .day-box{width:26px;height:22px;border:1.5px solid var(--ink)}
</style>
</head>
<body>
<main class="sheet">

  <section class="card card--front" aria-label="Business card front">
    <svg class="card-bg" viewBox="0 0 620 354" preserveAspectRatio="none" aria-hidden="true">
      <rect width="620" height="354" fill="var(--card-dark)"/>
      <path d="M0 200 C190 150 420 120 620 185 L620 354 L0 354Z" fill="var(--card-darker)"/>
      <path d="M0 200 C190 150 420 120 620 185" fill="none" stroke="var(--green)" stroke-width="4"/>
    </svg>
    <div class="brand"><span class="brand-dot"></span><span>Bright Path Wellness Centre</span></div>
    <div class="practitioner">
      <div class="practitioner-name">Dr. Marten Quovel B.Sc., D.C.</div>
      <div class="practitioner-title">Chiropractor</div>
      <div class="address">218 Farrow Gate<br>Westmere ON.<br>K2J 6P4</div>
    </div>
    <div class="divider"></div>
    <ul class="contact">
      <li><svg viewBox="0 0 16 16" aria-hidden="true"><path d="M3 1l3 3-2 2c1 2 3 4 5 5l2-2 3 3-2 2C7 14 2 9 1 3z" fill="var(--green)"/></svg>416-872-0196 (PATH)</li>
      <li><svg viewBox="0 0 16 16" aria-hidden="true"><circle cx="8" cy="8" r="6.5" fill="none" stroke="var(--green)" stroke-width="1.5"/><path d="M1.5 8h13M8 1.5c-3 3.5-3 9.5 0 13M8 1.5c3 3.5 3 9.5 0 13" fill="none" stroke="var(--green)" stroke-width="1.2"/></svg>www.brightpathwellnesscentre.example</li>
      <li><svg viewBox="0 0 16 16" aria-hidden="true"><rect x="1" y="3" width="14" height="10" fill="var(--green)"/><path d="M1 3l7 6 7-6" fill="none" stroke="var(--card-darker)" stroke-width="1.3"/></svg>brightpathchiro@mailbox.example</li>
    </ul>
  </section>

  <section class="card card--info" aria-label="Business card back with practice information">
    <svg class="card-bg" viewBox="0 0 620 354" preserveAspectRatio="none" aria-hidden="true">
      <rect width="620" height="354" fill="var(--card-dark)"/>
      <path d="M620 40 C610 200 520 300 390 354 L620 354Z" fill="var(--card-darker)"/>
      <path d="M620 40 C610 200 520 300 390 354" fill="none" stroke="var(--green)" stroke-width="4"/>
    </svg>
    <div class="brand"><span class="brand-dot brand-dot--lg"></span><span>Bright Path Wellness Centre</span></div>
    <div class="divider"></div>
    <div class="info-text">
      <p>There is more to chiropractic than the relief of headaches and back pain! Our primary focus is the integrity of your nerve system, which controls and regulates every cell and tissue of your body. The moving bones of the spinal column can impair this vital communication link between your brain and body. We help improve the function and structure of your spine, reducing nerve system compromise. The result? Even non-spinal related health problems can show improvement</p>
      <ul class="benefits">
        <li>Without drugs</li>
        <li>Without surgery</li>
        <li>Regardless of age</li>
        <li>for over a century</li>
        <li>Naturally</li>
      </ul>
    </div>
  </section>

  <section class="card card--appointment" aria-label="Appointment card back">
    <svg class="card-bg" viewBox="0 0 620 354" preserveAspectRatio="none" aria-hidden="true">
      <rect width="620" height="354" fill="var(--white)"/>
      <path d="M290 0 C430 10 560 60 620 150 L620 0Z" fill="var(--ink)"/>
      <path d="M340 0 C460 12 570 50 620 120 L620 0Z" fill="var(--green)"/>
      <path d="M620 185 C615 260 595 320 555 354 L620 354Z" fill="var(--green)"/>
      <path d="M610 150 C605 220 590 290 545 354" fill="none" stroke="var(--ink)" stroke-width="3"/>
    </svg>
    <div class="brand"><span class="brand-dot"></span><span>Bright Path Wellness Centre</span></div>
    <div class="field field--name"><span>Name :</span><span class="field-line"></span></div>
    <ul class="days">
      <li><span class="day-box"></span>M</li>
      <li><span class="day-box"></span>Tu</li>
      <li><span class="day-box"></span>W</li>
      <li><span class="day-box"></span>Th</li>
      <li><span class="day-box"></span>F</li>
      <li><span class="day-box"></span>Sat</li>
    </ul>
    <div class="field field--note"><span>Note :</span><span class="field-line"></span></div>
  </section>

</main>
</body>
</html>
```